Website for Excavator and Earthworks Company

We require a modern, sleek and practical website for our newly created earthworks/excavator business in Perth, Western Australia called Gullwind Stonecut Earthworks.

The website should have a modern, cutting edge feel but only needs to be relatively simplistic in it's layout and eventual functionality.

Some pages it should have would be Home, About, Projects and Contact Us.

Number of Pages Required

1 page

```html
<!DOCTYPE html>
<html lang="en">
<head>
<meta charset="utf-8">
<title>Gullwind Stonecut Earthworks</title>
<link href="https://fonts.googleapis.com/css2?family=Oswald:wght@500;700&family=Manrope:wght@300;400;600;700&display=swap" rel="stylesheet">
<style>
:root{
  --bg:#0b0b0d;
  --bg-soft:#131316;
  --lime:#b7e35c;
  --slate:#5f6d8a;
  --white:#f4f4f2;
  --muted:#8a8f99;
  --line:#26272c;
}
*{margin:0;padding:0;box-sizing:border-box}
html,body{width:1200px;height:1200px;overflow:hidden;background:var(--bg)}
body{font-family:"Manrope",sans-serif;color:var(--white);position:relative}
.site-nav{position:absolute;left:0;top:0;width:1200px;height:84px;display:flex;align-items:center;padding:0 60px;border-bottom:1px solid var(--line)}
.brand{display:flex;align-items:center;gap:12px;font-family:"Manrope",sans-serif;font-weight:700;font-size:17px;letter-spacing:1.5px;text-transform:uppercase;color:var(--white)}
.brand-mark{width:22px;height:22px;background:var(--lime);border-radius:3px}
.nav-links{display:flex;gap:34px;margin-left:auto;margin-right:40px;font-size:12px;font-weight:700;letter-spacing:1.5px}
.nav-links a{color:var(--white);text-decoration:none;padding-bottom:6px}
.nav-links a.active{color:var(--lime);border-bottom:2px solid var(--lime)}
.btn{display:inline-flex;align-items:center;gap:8px;height:42px;padding:0 26px;border-radius:22px;font-family:"Oswald",sans-serif;font-weight:500;font-size:13px;letter-spacing:1.5px;text-transform:uppercase}
.btn-lime{background:var(--lime);color:#121212;box-shadow:0 0 22px rgba(183,227,92,.35)}
.btn-ghost{border:1px solid #3a3b41;color:var(--white)}
.hero{position:absolute;left:0;top:84px;width:1200px;height:556px}
.eyebrow-pill{position:absolute;left:60px;top:44px;display:flex;align-items:center;gap:10px;padding:8px 16px;border:1px solid var(--line);border-radius:20px;background:var(--bg-soft);font-size:11px;letter-spacing:2.5px;font-weight:600;color:#cfd1d6}
.eyebrow-pill i{width:7px;height:7px;border-radius:50%;background:var(--lime)}
.hero-title{position:absolute;left:60px;top:104px;font-family:"Oswald",sans-serif;font-weight:700;font-size:104px;line-height:.98;text-transform:uppercase;letter-spacing:-1px}
.hero-title .accent{color:var(--lime);display:block}
.hero-lead{position:absolute;left:60px;top:336px;width:460px;font-size:19px;line-height:1.55;font-weight:300;color:#9aa0ab}
.hero-lead strong{font-weight:400;color:var(--white);display:block}
.hero-actions{position:absolute;left:60px;top:440px;display:flex;gap:16px}
.hero-media{position:absolute;left:630px;top:44px;width:510px;height:360px;border-radius:16px;background:linear-gradient(180deg,#aebccb 0%,#7f8fa0 40%,#4a3a35 62%,#2a2f3a 100%);box-shadow:0 20px 50px rgba(0,0,0,.6)}
.media-caption{position:absolute;left:20px;bottom:20px;padding:12px 18px;background:rgba(12,12,14,.88);border-radius:10px;border-left:3px solid var(--lime)}
.media-caption small{display:block;font-size:10px;letter-spacing:2px;color:var(--lime);font-weight:700}
.media-caption span{font-family:"Oswald",sans-serif;font-size:17px}
.scroll-cue{position:absolute;left:596px;top:470px;display:flex;flex-direction:column;align-items:center;gap:8px;font-size:9px;letter-spacing:2px;color:var(--muted)}
.scroll-cue b{width:1px;height:46px;background:linear-gradient(var(--lime),transparent)}
.about{position:absolute;left:0;top:640px;width:1200px;height:560px;border-top:1px solid var(--line)}
.about-media{position:absolute;left:60px;top:70px;width:470px;height:330px;border-radius:12px;background:linear-gradient(160deg,#5e6a70 0%,#3a4248 50%,#23292e 100%)}
.badge{position:absolute;right:-20px;bottom:-20px;width:112px;height:92px;background:var(--lime);color:#111;border-radius:8px;padding:16px 14px}
.badge strong{font-family:"Oswald",sans-serif;font-size:28px;line-height:1;display:block}
.badge small{font-size:9px;font-weight:700;letter-spacing:1px}
.badge svg{position:absolute;right:12px;top:14px}
.about-copy{position:absolute;left:620px;top:50px;width:520px}
.eyebrow{display:flex;align-items:center;gap:12px;font-size:11px;letter-spacing:3px;font-weight:700;color:var(--lime)}
.eyebrow::before{content:"";width:26px;height:1px;background:var(--muted)}
.about-title{margin-top:14px;font-family:"Oswald",sans-serif;font-weight:700;font-size:52px;line-height:1;text-transform:uppercase}
.about-title span{display:block;color:var(--slate)}
.about-text{margin-top:22px;font-size:14px;line-height:1.7;color:#b8bcc4;font-weight:300}
.features{margin-top:30px;list-style:none;display:flex;flex-direction:column;gap:26px}
.feature{display:flex;gap:16px}
.feature svg{flex:none;margin-top:2px}
.feature h3{font-family:"Oswald",sans-serif;font-weight:500;font-size:16px}
.feature p{font-size:12.5px;color:#6e7e9e;margin-top:4px}
</style>
</head>
<body>
<header class="site-nav">
  <div class="brand"><span class="brand-mark"></span>Gullwind Stonecut</div>
  <nav class="nav-links">
    <a href="#">HOME</a><a href="#" class="active">ABOUT</a><a href="#">SERVICES</a><a href="#">PROJECTS</a><a href="#">CONTACT</a>
  </nav>
  <span class="btn btn-lime">Get a Quote</span>
</header>

<section class="hero">
  <div class="eyebrow-pill"><i></i>PERTH, WA • EST 2024</div>
  <h1 class="hero-title">Precision<span class="accent">Earthworks</span></h1>
  <p class="hero-lead">High-grade excavation and civil solutions.<strong>Engineered for accuracy. Built for speed.</strong></p>
  <div class="hero-actions">
    <span class="btn btn-lime">Request a Quote
      <svg width="14" height="14" viewBox="0 0 14 14"><path d="M2 7h10M8 3l4 4-4 4" stroke="#121212" stroke-width="1.8" fill="none"/></svg></span>
    <span class="btn btn-ghost">View Capabilities</span>
  </div>
  <div class="hero-media" role="img" aria-label="Photo of a container port with cranes and stacked shipping containers">
    <div class="media-caption"><small>FLEET READY</small><span>Heavy Excavation</span></div>
  </div>
  <div class="scroll-cue">SCROLL<b></b></div>
</section>

<section class="about">
  <div class="about-media" role="img" aria-label="Aerial photo of workers in hi-vis gear laying steel reinforcement on a site">
    <div class="badge">
      <strong>100%</strong><small>WA OWNED</small>
      <svg width="12" height="12" viewBox="0 0 12 12"><path d="M2 10L10 2M4 2h6v6" stroke="#111" stroke-width="1.6" fill="none"/></svg>
    </div>
  </div>
  <div class="about-copy">
    <div class="eyebrow">THE STANDARD</div>
    <h2 class="about-title">Grounded in<span>Performance.</span></h2>
    <p class="about-text">Gullwind Stonecut Earthworks was established to bring a higher tier of reliability to the Perth excavation industry. We treat every cubic metre of earth with engineering precision.</p>
    <ul class="features">
      <li class="feature">
        <svg width="18" height="18" viewBox="0 0 18 18"><path d="M9 1.5l6 2.5v5c0 3.5-2.6 6.3-6 7.5-3.4-1.2-6-4-6-7.5V4z M6 9l2 2 4-4" stroke="var(--lime)" stroke-width="1.5" fill="none"/></svg>
        <div><h3>Safety First</h3><p>Rigorous safety protocols ensuring compliant, hazard-free worksites.</p></div>
      </li>
      <li class="feature">
        <svg width="18" height="18" viewBox="0 0 18 18"><path d="M3 13L13 3l2 2L5 15H3z M11 5l2 2" stroke="var(--lime)" stroke-width="1.5" fill="none"/></svg>
        <div><h3>Laser Precision</h3><p>Advanced levelling and site prep accurate to the millimetre.</p></div>
      </li>
      <li class="feature">
        <svg width="18" height="18" viewBox="0 0 18 18"><circle cx="9" cy="9" r="7" stroke="var(--lime)" stroke-width="1.5" fill="none"/><path d="M9 5v4l3 2" stroke="var(--lime)" stroke-width="1.5" fill="none"/></svg>
        <div><h3>Reliable Timelines</h3><p>We deliver on schedule. No excuses, just progress.</p></div>
      </li>
    </ul>
  </div>
</section>
</body>
</html>
```